Beekeeper needs box/label design for honey/CBD and other honey-related products

We need a box (or label) design for a beekeeping company in Virginia called Tamsin Hollow Farm. Our products will include honey mixed with CBD oil and other essential oils (vanilla, lavender, etc).The box design should be scalable to include several different honey/oil products. We would like to incorporate our current farm logo into the design. Here is a link to a honey producing company with a series of products using their honey mixed with certain oils. It's a good reference of what type box/label design we would like (https://corbinandlyle.co/pages/honey).

Target Market(s)

Retail stores and consumers

Requirements
Must have
• Tamsin Hollow Farm name and logo

```html
<!DOCTYPE html>
<html lang="en">
<head>
<meta charset="utf-8">
<title>Tamsin Hollow Farm – Raw Honey with CBD Oil and Lavender label</title>
<link rel="stylesheet" href="https://fonts.googleapis.com/css2?family=Cormorant+Garamond:wght@500&family=Crimson+Text:wght@400;600&family=Yellowtail&family=Courgette&display=swap">
<style>
  :root {
    --page: #ffffff;
    --label-top: #efe3da;
    --label-bottom: #dccbbf;
    --olive: #7d7c45;
    --olive-mark: #93a23b;
    --rule-olive: #8d8f60;
    --ink: #1f1f1f;
    --ink-soft: #555555;
    --lavender: #4a4f9f;
    --lavender-faint: #d9d3e4;
  }
  * { margin: 0; padding: 0; box-sizing: border-box; }
  html, body {
    width: 1200px;
    height: 1200px;
    overflow: hidden;
    background: var(--page);
  }
  .canvas {
    position: relative;
    width: 1200px;
    height: 1200px;
  }
  .label {
    position: absolute;
    left: 232px;
    top: 137px;
    width: 735px;
    height: 925px;
    background: linear-gradient(180deg, var(--label-top) 0%, var(--label-bottom) 100%);
    font-family: "Crimson Text", serif;
    color: var(--ink);
  }
  .label > * { position: absolute; }
  .brand-mark {
    left: 278px;
    top: 48px;
    width: 185px;
    height: 185px;
    background: var(--olive-mark);
  }
  .brand-name {
    left: 0;
    width: 100%;
    top: 262px;
    text-align: center;
    font-family: "Cormorant Garamond", serif;
    font-weight: 500;
    font-size: 44px;
    letter-spacing: 4px;
    color: var(--olive);
  }
  .product-title {
    left: 148px;
    top: 442px;
    font-size: 72px;
    line-height: 1;
    white-space: nowrap;
  }
  .product-title .raw { color: var(--ink-soft); }
  .product-title .honey { color: var(--ink); }
  .title-rule {
    left: 140px;
    top: 520px;
    width: 443px;
    height: 3px;
    background: var(--rule-olive);
  }
  .with-cbd {
    left: 240px;
    top: 532px;
    font-size: 50px;
    line-height: 1;
    white-space: nowrap;
  }
  .with-cbd .with { font-size: 40px; }
  .initial {
    left: 160px;
    top: 570px;
    font-size: 200px;
    line-height: 1;
    color: var(--lavender-faint);
  }
  .and {
    left: 484px;
    top: 600px;
    font-size: 32px;
    line-height: 1;
  }
  .flavour {
    left: 302px;
    top: 655px;
    font-family: "Yellowtail", cursive;
    font-size: 60px;
    line-height: 1;
    color: var(--lavender);
  }
  .flavour-rule {
    left: 280px;
    top: 728px;
    width: 295px;
    border-top: 1.5px dashed var(--ink);
  }
  .tagline {
    left: 67px;
    width: 600px;
    top: 748px;
    text-align: center;
    font-family: "Courgette", cursive;
    font-size: 21px;
    line-height: 36px;
    color: #333333;
  }
  .footer-rule {
    left: 180px;
    top: 832px;
    width: 395px;
    height: 1.5px;
    background: var(--ink);
  }
  .net-weight {
    left: 0;
    width: 100%;
    top: 852px;
    text-align: center;
    font-size: 24px;
  }
</style>
</head>
<body>
<div class="canvas">
  <div class="label">
    <div class="brand-mark"></div>
    <div class="brand-name">TAMSIN HOLLOW FARM</div>

    <h1 class="product-title"><span class="raw">RAW</span> <span class="honey">HONEW</span></h1>
    <div class="title-rule"></div>
    <div class="with-cbd"><span class="with">with</span> CBD OIL</div>

    <div class="initial">L</div>
    <div class="and">and</div>
    <div class="flavour">Lavender</div>
    <div class="flavour-rule"></div>

    <p class="tagline">Excellent tonic for stress and anxiety due to<br>its relaxing nature and wonderful scent</p>
    <div class="footer-rule"></div>
    <div class="net-weight">Net. Wt. 500 g</div>
  </div>
</div>
</body>
</html>
```